Event Poster - Tarona Mist Fest 2018 (Need ASAP)

Create a poster for an upcoming vape event, located in Tarona, Hamilton, New Zealand.

Mist Fest is an event where lots of shops come to a location, and the public are welcomed and they all vape, buy vape products, socialize, drink beer and have fun.

VISIT THE EVENT WEBSITE FOR INFO - www.taronamistfest.co.nz

We have created a website at, as you can see the logo and design is a bit boring and plain, so we dont really want it to look anything like that, The logo that is created to suit the poster will be able to be

Need a poster done up so we can send it around, post it up on boards, share on social media etc

I have attached previous events from nearby towns, for reference, but I want something much better.

Target Market(s)

25-45 Male / Female

Requirements
Must have
• - Tarona Mist Fest 2018
• - Saturday, 2nd June 2018
• - 12-10pm
• - R18 Event (important for public to know)
• - Vendors, Prizes, Comps, E Juice Awards, Entertainment, Giveaways & More
• - The Corner Alehouse (52 Mulgrave Rd, Kerepuni, Hamilton)
• - mention something along lines "Come To Tarona's First Mist Fest"
• - "Get Your Tickets from www.taronamistfest.co.nz TODAY"
• - I want people to know they can buy it from a store as well "The Cloud Barn"
Nice to have
• Our City colors are Red,Yellow,Black which is symbolic for "Tarona" so it would be nice to have those integrated in there. Alot of the other Mist Fest events have dark, bogan, amateur look done to them, so I want ours to be just a much better version.
• To Clarify, Hamilton is a city inside the Tarona
• I might want to put sponsors on there as well, possibly 10-20, but maybe only a few if space is a problem

```html
<!DOCTYPE html>
<html lang="en">
<head>
<meta charset="utf-8">
<title>Tarona Mist Fest 2018</title>
<link href="https://fonts.googleapis.com/css2?family=Baloo+2:wght@600;800&family=Questrial&display=swap" rel="stylesheet">
<style>
  :root {
    --black: #000000;
    --white: #ffffff;
    --yellow: #f6c400;
    --amber: #f08a10;
    --orange: #e2620e;
    --red: #e3141b;
    --deep-red: #8a1208;
    --head: "Baloo 2", sans-serif;
    --body: "Questrial", sans-serif;
  }
  * { margin: 0; padding: 0; box-sizing: border-box; }
  html, body { width: 849px; height: 1200px; overflow: hidden; background: var(--black); }
  .poster {
    position: relative; width: 849px; height: 1200px; overflow: hidden;
    background: var(--black); color: var(--white); font-family: var(--head);
  }
  .smoke-art {
    position: absolute; inset: 0;
    background:
      radial-gradient(ellipse 260px 420px at 640px 260px, rgba(246,196,0,.55), transparent 70%),
      radial-gradient(ellipse 300px 260px at 560px 560px, rgba(240,138,16,.5), transparent 70%),
      radial-gradient(ellipse 260px 360px at 230px 760px, rgba(227,20,27,.45), transparent 72%),
      radial-gradient(ellipse 200px 300px at 780px 120px, rgba(246,196,0,.35), transparent 70%),
      radial-gradient(ellipse 220px 200px at 120px 980px, rgba(138,18,8,.5), transparent 70%),
      var(--black);
  }
  .event-mark {
    position: absolute; left: 97px; top: 108px;
    display: flex; align-items: flex-end; gap: 8px;
  }
  .event-mark .mark-square { width: 100px; height: 178px; background: var(--yellow); }
  .event-mark .mark-name {
    font-family: var(--head); font-weight: 800; color: var(--white);
    font-size: 48px; line-height: .98; white-space: nowrap;
  }
  .day { position: absolute; left: 40px; top: 346px; font-size: 40px; font-weight: 800; line-height: 1.2; }
  .date {
    position: absolute; left: 36px; top: 384px; font-size: 138px; font-weight: 800;
    line-height: 1; white-space: nowrap;
  }
  .date sup { font-size: 60px; vertical-align: 58px; margin-left: 2px; margin-right: 14px; }
  .time {
    position: absolute; right: 40px; top: 514px; font-size: 78px; font-weight: 800; line-height: 1;
  }
  .venue { position: absolute; left: 40px; top: 596px; }
  .venue-name { font-family: var(--body); font-size: 37px; -webkit-text-stroke: .9px var(--white); line-height: 1.2; }
  .venue-address { font-family: var(--body); font-size: 23px; letter-spacing: .5px; margin-top: 2px; }
  .age-limit {
    position: absolute; right: 28px; top: 712px; color: var(--red);
    font-size: 36px; font-weight: 800; line-height: 1.2;
  }
  .features {
    position: absolute; left: 40px; top: 758px; font-size: 40px; font-weight: 800; line-height: 56px;
    white-space: nowrap;
  }
  .tickets {
    position: absolute; left: 10px; top: 1020px; width: 430px; text-align: center;
    font-family: var(--body); font-size: 25px; line-height: 36px; white-space: nowrap;
  }
  .tickets .invite { font-family: var(--head); font-weight: 800; color: var(--yellow); font-size: 24px; }
  .tickets .site { font-weight: 800; font-family: var(--head); font-size: 29px; letter-spacing: .5px; }
  .tickets .store strong { font-family: var(--head); font-weight: 800; }
  .sponsor-ring { position: absolute; inset: 0; }
  .sponsors { position: absolute; inset: 0; }
  .sponsor {
    position: absolute; width: 112px; text-align: center; transform: translateX(-50%);
    font-family: var(--head); font-weight: 600; color: var(--white); font-size: 11px; line-height: 1.15;
    white-space: nowrap;
  }
  .sponsor .dot {
    display: block; width: 58px; height: 58px; margin: 0 auto 5px;
    border-radius: 50%; border: 2px solid var(--white);
  }
  .sponsor.lead { font-size: 15px; letter-spacing: 2px; width: 200px; }
</style>
</head>
<body>
<main class="poster">
  <div class="smoke-art" role="img" aria-label="Flowing mesh of smoke ribbons in yellow, orange and red on black"></div>

  <div class="event-mark">
    <span class="mark-square"></span>
    <span class="mark-name">Tarona<br>Mist Fest<br>2018</span>
  </div>

  <div class="day">Saturday</div>
  <div class="date">2<sup>nd</sup>June 2018</div>
  <div class="time">12-10 pm</div>

  <div class="venue">
    <div class="venue-name">The Corner Alehouse</div>
    <div class="venue-address">(52 Mulgrave Rd, Kerepuni, Hamilton)</div>
  </div>

  <div class="age-limit">R18</div>

  <div class="features">
    Vendors, Prizes, Comps,<br>
    E Juice Awards,<br>
    Entertainment,<br>
    Giveaways &amp; More
  </div>

  <div class="tickets">
    <div class="invite">Come To Tarona's First Mist Fest</div>
    <div>Get Your Tickets TODAY!</div>
    <div class="site">www.taronamistfest.co.nz</div>
    <div class="store">stores &nbsp;<strong>"The Cloud Barn"</strong></div>
  </div>

  <svg class="sponsor-ring" width="849" height="1200" viewBox="0 0 849 1200" aria-hidden="true">
    <defs>
      <path id="sponsor-arc" d="M 480 971 A 328 328 0 0 1 620 829"/>
    </defs>
    <circle cx="772" cy="1120" r="317" fill="var(--black)" stroke="var(--orange)" stroke-width="2"/>
    <text font-family="Baloo 2, sans-serif" font-weight="800" font-size="12" letter-spacing="1.5" fill="var(--orange)">
      <textPath href="#sponsor-arc">SOME SPONSORS :</textPath>
    </text>
  </svg>

  <section class="sponsors" aria-label="Sponsors">
    <div class="sponsor lead" style="left:697px; top:836px;">NIMBUS VAPES</div>
    <div class="sponsor" style="left:567px; top:896px;"><span class="dot"></span>Kettle Vape House</div>
    <div class="sponsor" style="left:678px; top:896px;"><span class="dot"></span>Drift House</div>
    <div class="sponsor" style="left:789px; top:896px;"><span class="dot"></span>Liquid Lounge</div>
    <div class="sponsor" style="left:567px; top:994px;"><span class="dot"></span>Haze Acre</div>
    <div class="sponsor" style="left:678px; top:994px;"><span class="dot"></span>Blend Fine Liquids</div>
    <div class="sponsor" style="left:789px; top:994px;"><span class="dot"></span>Reel Juice</div>
    <div class="sponsor" style="left:567px; top:1094px;"><span class="dot"></span>Bramble Liquid Co</div>
    <div class="sponsor" style="left:678px; top:1094px;"><span class="dot"></span>True Vapes</div>
    <div class="sponsor" style="left:789px; top:1094px;"><span class="dot"></span>Shaker Supply</div>
  </section>
</main>
</body>
</html>
```